New Business Card Design Project

I would like my card design to look exactly like the logo, design, layout, and print of the current attached file. The only change I would like made would be for the print to say THE KMW GROUP instead of THE HALLORAN GROUP. Basically, just replace his group name with my group name. I would also like the backgroud to be the same texture and color as the attached file. I love the dark blue lettering and house logo on the card.

I am completely open to the rest of the card design. I just want something clean and simple. Only basic contact info required on the card. Maybe just name: Kyle M Warrick and cell # 555.914.2087 and email kyle@orchidhomesagent.com

```html
<!DOCTYPE html>
<html lang="en">
<head>
<meta charset="utf-8">
<title>Kyle M Warrick – The KMW Group</title>
<link rel="stylesheet" href="https://fonts.googleapis.com/css2?family=Libre+Franklin:wght@700&family=Montserrat:wght@400&display=swap">
<style>
  :root {
    --navy: #0f0f2a;
    --paper: #ffffff;
    --silver-light: #e4e4e4;
    --silver-dark: #555555;
  }
  html, body {
    margin: 0;
    padding: 0;
    overflow: hidden;
    background: var(--paper);
  }
  .card {
    position: relative;
    width: 1200px;
    height: 686px;
    background: var(--paper);
    overflow: hidden;
    color: var(--navy);
  }
  .swoosh {
    position: absolute;
    inset: 0;
    width: 1200px;
    height: 686px;
  }
  .brand {
    position: absolute;
    left: 800px;
    top: 68px;
    display: flex;
    align-items: center;
    gap: 48px;
  }
  .brand-square {
    width: 100px;
    height: 100px;
    background: var(--navy);
  }
  .brand-name {
    margin: 0;
    font-family: "Montserrat", sans-serif;
    font-weight: 400;
    font-size: 35px;
    line-height: 41px;
    letter-spacing: 6px;
    color: var(--navy);
  }
  .brand-name span { display: block; }
  .agent-name {
    position: absolute;
    left: 101px;
    top: 284px;
    margin: 0;
    padding-left: 11px;
    border-left: 3px solid var(--navy);
    font-family: "Libre Franklin", sans-serif;
    font-weight: 700;
    font-size: 70px;
    line-height: 74px;
    letter-spacing: -0.5px;
  }
  .contact {
    position: absolute;
    left: 108px;
    top: 518px;
    margin: 0;
    padding: 0;
    list-style: none;
    font-family: "Montserrat", sans-serif;
    font-weight: 400;
    font-size: 30px;
    line-height: 42px;
  }
  .contact li {
    display: flex;
    align-items: center;
    gap: 10px;
  }
  .contact svg {
    width: 28px;
    height: 28px;
    fill: var(--navy);
  }
</style>
</head>
<body>
<main class="card">
  <svg class="swoosh" viewBox="0 0 1200 686" aria-hidden="true">
    <defs>
      <linearGradient id="silver-top" x1="0" y1="0" x2="1" y2="1">
        <stop offset="0" stop-color="var(--silver-dark)"/>
        <stop offset="0.55" stop-color="var(--silver-light)"/>
        <stop offset="1" stop-color="#9a9a9a"/>
      </linearGradient>
      <linearGradient id="silver-bottom" x1="1" y1="0" x2="0" y2="1">
        <stop offset="0" stop-color="var(--silver-light)"/>
        <stop offset="0.5" stop-color="#a8a8a8"/>
        <stop offset="1" stop-color="var(--silver-dark)"/>
      </linearGradient>
    </defs>
    <path d="M0,0 H300 Q110,85 0,285 Z" fill="url(#silver-top)"/>
    <path d="M0,0 H232 Q70,62 0,200 Z" fill="var(--navy)"/>
    <path d="M1200,145 Q1115,570 668,686 H1200 Z" fill="url(#silver-bottom)"/>
    <path d="M1200,286 Q1105,610 705,686 H1200 Z" fill="var(--navy)"/>
  </svg>

  <div class="brand">
    <div class="brand-square" aria-hidden="true"></div>
    <p class="brand-name"><span>THE</span><span>KMW</span><span>GROUP</span></p>
  </div>

  <h1 class="agent-name">Kyle M Warrick</h1>

  <ul class="contact">
    <li>
      <svg viewBox="0 0 24 24" aria-hidden="true"><path d="M6.6 10.8a15.2 15.2 0 0 0 6.6 6.6l2.2-2.2a1 1 0 0 1 1-.25 11.4 11.4 0 0 0 3.6.57 1 1 0 0 1 1 1V20a1 1 0 0 1-1 1A17 17 0 0 1 3 4a1 1 0 0 1 1-1h3.5a1 1 0 0 1 1 1c0 1.25.2 2.45.57 3.57a1 1 0 0 1-.25 1z"/></svg>
      <span>I 555.914.2087</span>
    </li>
    <li>
      <svg viewBox="0 0 24 24" aria-hidden="true"><path d="M2 5h20v14H2z M2 5l10 8 10-8" fill="none" stroke="var(--navy)" stroke-width="0"/><path d="M2 5h20L12 12.5z"/><path d="M2 7l10 7.5L22 7v12H2z"/></svg>
      <span>I kyle@orchidhomesagent.com</span>
    </li>
  </ul>
</main>
</body>
</html>
```